Quote Cards With TK May 2025 for Instagram

I would like to put these quotes over one of the pictures attached; Instagram (new size: 4:5 (1080 x 1350 pixels) One Quote per picture, and I want the quote to be bold or easy to read as well. I provided a few reference graphics that I really like as examples below. In very small letters at the bottom add @TKBarlowOnline

All of the pictures are attached; you can pick any photo and add one quote to it; but no stock photography

```html
<!DOCTYPE html>
<html lang="en">
<head>
<meta charset="utf-8">
<title>Quote Cards With TK</title>
<link href="https://fonts.googleapis.com/css2?family=Barlow+Condensed:wght@600&family=Open+Sans:wght@300&display=swap" rel="stylesheet">
<style>
  :root {
    --page: #ffffff;
    --magenta: #e0006f;
    --hot-pink: #ff14a6;
    --soft-pink: #f68bd0;
    --near-black: #241a1d;
    --quote-white: #f4f1f2;
    --quote-grey: #d9d4d8;
    --panel: rgba(240, 150, 205, 0.82);
    --photo-light: #8a6a52;
    --photo-dark: #2a2224;
  }
  * { margin: 0; padding: 0; box-sizing: border-box; }
  html, body { width: 1200px; height: 811px; overflow: hidden; background: var(--page); }
  .board { position: relative; width: 1200px; height: 811px; }
  .quote-card { position: absolute; width: 344px; height: 430px; overflow: hidden; }
  .card-dark-magenta { left: 78px; top: 217px; background: radial-gradient(ellipse 60% 62% at 55% 40%, var(--magenta) 0%, #8a0a48 55%, var(--near-black) 100%); }
  .card-dark-blush { left: 446px; top: 218px; background: radial-gradient(ellipse 62% 70% at 70% 45%, var(--soft-pink) 0%, #b05a94 48%, var(--near-black) 100%); }
  .card-hot-pink { left: 822px; top: 219px; background: radial-gradient(ellipse 55% 62% at 55% 40%, #ff9ad6 0%, #ff5cc0 45%, var(--hot-pink) 100%); }
  .portrait {
    position: absolute; top: 32px; width: 180px; bottom: 0;
    border-radius: 70px 70px 10px 10px;
    background: linear-gradient(180deg, var(--photo-dark) 0%, var(--photo-light) 30%, #6e5240 62%, var(--photo-dark) 70%, #141012 100%);
  }
  .card-dark-magenta .portrait { left: 82px; }
  .card-dark-blush .portrait, .card-hot-pink .portrait { left: 26px; }
  .quote {
    font-family: "Barlow Condensed", "Arial Narrow", sans-serif;
    font-weight: 600; text-transform: uppercase; white-space: nowrap;
    font-size: 21px; line-height: 21px; letter-spacing: 0.2px;
  }
  .quote-open { position: absolute; left: 72px; top: 299px; color: var(--quote-white); }
  .quote-panel { position: absolute; left: 107px; top: 221px; width: 231px; height: 133px; background: var(--panel); overflow: hidden; }
  .quote-panel .quote { position: absolute; left: 12px; top: 25px; color: var(--quote-grey); font-size: 22px; line-height: 21.5px; }
  .handle {
    position: absolute; font-family: "Open Sans", Arial, sans-serif; font-weight: 300;
    font-size: 11px; color: var(--quote-white);
  }
  .card-dark-magenta .handle { left: 252px; top: 400px; }
  .card-dark-blush .handle { left: 225px; top: 372px; color: #a88a9c; }
  .card-hot-pink .handle { left: 225px; top: 372px; color: #5a1c40; }
</style>
</head>
<body>
<main class="board">
  <section class="quote-card card-dark-magenta">
    <div class="portrait" role="img" aria-label="Photo of TK smiling in a sparkly brown turtleneck and black trousers"></div>
    <p class="quote quote-open">Tired. Moody. Stubborn<br>Belly fat&nbsp; Your hormones<br>are screaming for help!<br>Let’s fix that.</p>
    <p class="handle">@TKBarlowOnline</p>
  </section>

  <section class="quote-card card-dark-blush">
    <div class="portrait" role="img" aria-label="Photo of TK smiling in a sparkly brown turtleneck and black trousers"></div>
    <div class="quote-panel">
      <p class="quote">Tired. Moody. Stubborn<br>Belly fat&nbsp; Your hormones<br>are screaming for help!<br>Let’s fix that.</p>
    </div>
    <p class="handle">@TKBarlowOnline</p>
  </section>

  <section class="quote-card card-hot-pink">
    <div class="portrait" role="img" aria-label="Photo of TK smiling in a sparkly brown turtleneck and black trousers"></div>
    <div class="quote-panel">
      <p class="quote">Tired. Moody. Stubborn<br>Belly fat&nbsp; Your hormones<br>are screaming for help!<br>Let’s fix that.</p>
    </div>
    <p class="handle">@TKBarlowOnline</p>
  </section>
</main>
</body>
</html>
```